Business Card Design

Very plain simple card, Plain modern font. Background. Grey fading to black. Large Bright lime green text. Saying.

TWR-ZA.COM

Small other details in white text.

Irish Horse Sales . Livery . Stud . Shows

Mark Dabrowski
TWR
Birch Lodge
Carrowmede Lane
Thistlecombe
Lincolnshire
LN4 7JX

Email. Twrzap@mailvale.co.uk
Tel. 07482 936504

Industry/Entity Type

Business

Contact Information for Business Card

As below

```html
<!DOCTYPE html>
<html lang="en">
<head>
<meta charset="utf-8">
<title>TWR-ZA.COM Business Card</title>
<link href="https://fonts.googleapis.com/css2?family=Exo+2:wght@200;300;400&display=swap" rel="stylesheet">
<style>
  :root {
    --canvas: #f2f2f4;
    --lime: #aecc36;
    --navy: #022e45;
    --sweep: #3e5a4f;
    --white: #f4f6f7;
  }
  * { margin: 0; padding: 0; box-sizing: border-box; }
  html, body {
    width: 1200px;
    height: 1000px;
    overflow: hidden;
    background: var(--canvas);
    font-family: "Exo 2", sans-serif;
  }
  .canvas { position: relative; width: 1200px; height: 1000px; }
  .card { position: absolute; width: 512px; height: 290px; overflow: hidden; }
  .card-front { left: 344px; top: 153px; background: var(--lime); }
  .card-back { left: 343px; top: 513px; background: var(--navy); }
  .sweep { position: absolute; left: 0; top: 0; width: 512px; height: 290px; }
  .front-mark {
    position: absolute;
    left: 0; right: 0; top: 122px;
    text-align: center;
    color: var(--navy);
    font-weight: 400;
    font-size: 30px;
    letter-spacing: 3px;
  }
  .brand-name {
    position: absolute;
    left: 0; right: 0; top: 22px;
    text-align: center;
    color: var(--lime);
    font-weight: 200;
    font-size: 54px;
    letter-spacing: 2px;
    line-height: 64px;
  }
  .services {
    position: absolute;
    left: 0; right: 0; top: 109px;
    text-align: center;
    color: var(--white);
    font-weight: 300;
    font-size: 15px;
    letter-spacing: 0.3px;
  }
  .contact {
    position: absolute;
    top: 215px;
    display: flex;
    align-items: center;
    color: var(--white);
    font-weight: 300;
    font-size: 15px;
  }
  .contact-email { left: 41px; }
  .contact-phone { left: 305px; }
  .bars {
    display: inline-block;
    width: 14px; height: 24px;
    margin-right: 5px;
    border-left: 3px solid var(--lime);
    border-right: 3px solid var(--lime);
  }
</style>
</head>
<body>
<div class="canvas">
  <section class="card card-front">
    <svg class="sweep" viewBox="0 0 512 290" aria-hidden="true">
      <path fill="var(--sweep)" d="M0,32 C30,80 78,120 78,190 C78,240 55,265 35,290 L28,290 C40,270 56,245 58,210 C60,160 30,120 0,85 Z"/>
    </svg>
    <div class="front-mark">TWR-ZA.COM</div>
  </section>

  <section class="card card-back">
    <svg class="sweep" viewBox="0 0 512 290" aria-hidden="true">
      <path fill="var(--sweep)" d="M512,0 C490,30 440,90 435,150 C432,200 465,235 485,255 C460,225 445,190 455,140 C465,100 500,60 512,45 Z"/>
    </svg>
    <h1 class="brand-name">TWR-ZA.COM</h1>
    <p class="services">Irish Horse Sales . Livery . Stud . Shows</p>
    <p class="contact contact-email"><span class="bars"></span>Email. Twrzap@mailvale.co.uk</p>
    <p class="contact contact-phone"><span class="bars"></span>Tel. 07482 936504</p>
  </section>
</div>
</body>
</html>
```